TROMP Diagnostics App - iOS

I need some UI artwork (2D) for my already released iOS app: "TROMP Kv" I'd like the UI to look more like an in-dash head-unit in a car. I'm in the process of updating the app with iPad support and would like to release this next version with a brand new UI.

A lot of car audio enthusiast already use my app and probably mount their iPhone/iPod near their car audio components on the dash. Most of the car audio deck Mfgs support a few colors: Green/Blue/Amber/Red I'd like to offer these themes as well. But I will settle for the Amber color to match my existing App icon scheme. (nice to have)

My UI is incredibly simple. It's just a bunch of up/down buttons. I plan to do some animations an will need some room blocked off for this to the left of LCD text.

Screenshots are of my existing iOS app for iPhone and the half assed job I did for iPad. - Note: These are the only two orientations I plan to use. But the resolution in these photos are smaller than my requirements. See "Must Haves" for all four resolutions.

update: I'd like something to imitate the style of the skin in the following: http://quorvak.pelmintra.example/art/Lumatone-XJR8-Skin-71845206

Thanks!

Target Market(s)

Car Audio Enthusiasts

Industry/Entity Type

Audio

Requirements
Must have
• - Static background that looks like an in-dash stereo. (think lumatone skin)
- An LCD area where I can display some text and stats on left (see iPad ss)
- UI buttons that support up/down states. When the user presses a button, it stays "down" until it's tapped again or another is pushed.
- UI toggle switch for Wobble mode (see ss)

iPhone/iPod resolutions
-
- Landscape for iPhone4/4S Retina (960 x 640)
- Landscape for iPhone 5 Retina (1136 x 640)

iPad resolutions
-
- This UI has more buttons and taller, but I'd like a similar look and feel
- Landscape for iPad Retina (2048 x 1536)
- Landscape for iPad2/mini (1024 x 768)

Other Controls:
- An empty space for UI slider control. I will place this over artwork. (see ss)
- Emergency stop button should be red and easily accessible. Slightly larger than other buttons.

iPhone Buttons/Controls
-
20,30,40,50,60,70,80,90,100,150,250,300
Toggle Switch, P button, S button, Stop button

iPad Buttons/Controls
-
20,25,30,35,40,45,50,55,60,65,70,80,90,110,125,150,250,300
Instant TROMP Buttons: 20,25,30,35,40,45,50,55

Disregard the waveform animation in the screenshots (squiggly line at bottom) I plan do a small animation to the left of the text in the LCD area.
Nice to have
• - Theme for LED-like colors: Green/Blue/Amber/Red on-off buttons
Should not have
• - sharp corners on buttons
- stretched version of iPhone layout for the iPad.

```html
<!DOCTYPE html>
<html lang="en">
<head>
<meta charset="utf-8">
<title>TROMP Kv – Head-Unit Themes</title>
<link href="https://fonts.googleapis.com/css2?family=Arimo:wght@400;700&family=Share+Tech+Mono&display=swap" rel="stylesheet">
<style>
  :root{
    --canvas:#000;
    --status-text:#fff;
    --digit:#e4e4e4;
    --label:#f2f2f2;
    --frame-line:#5a5a5a;
  }
  .theme-green{--hi:#36e040;--mid:#0b8f17;--lo:#023a08;--deep:#011a04;--glow:rgba(0,220,40,.45);--thumb:#22f02e;--stop-top:#ff4a3a;--stop-bot:#a80000;--stop-text:#2a0000;}
  .theme-graphite{--hi:#4e4e4e;--mid:#2b2b2b;--lo:#111;--deep:#080808;--glow:rgba(255,255,255,.08);--thumb:#555;--stop-top:#ff4a3a;--stop-bot:#a80000;--stop-text:#2a0000;}
  .theme-blue{--hi:#49a6ff;--mid:#0b58cc;--lo:#03205e;--deep:#010c2a;--glow:rgba(20,120,255,.45);--thumb:#d0d0d0;--stop-top:#ff4a3a;--stop-bot:#a80000;--stop-text:#2a0000;}
  .theme-red{--hi:#ff4040;--mid:#b20909;--lo:#3c0000;--deep:#1a0000;--glow:rgba(255,20,20,.45);--thumb:#ff1a1a;--stop-top:#ffffff;--stop-bot:#9a9a9a;--stop-text:#111;}

  html,body{margin:0;padding:0;overflow:hidden;}
  body{width:1200px;height:800px;background:var(--canvas);position:relative;font-family:"Arimo",Arial,sans-serif;}

  .screen{position:absolute;width:538px;height:358px;box-sizing:border-box;border:1px solid var(--frame-line);
    background:radial-gradient(ellipse at 50% 45%,var(--glow) 0%,rgba(0,0,0,0) 70%),#000;overflow:hidden;}
  .screen--tl{left:52px;top:35px;}
  .screen--tr{left:620px;top:35px;}
  .screen--bl{left:52px;top:418px;}
  .screen--br{left:620px;top:418px;}

  .status-bar{position:absolute;left:0;top:0;width:100%;height:22px;background:#000;color:var(--status-text);font-size:13px;font-weight:700;}
  .status-bar__signal{position:absolute;left:8px;top:6px;display:flex;align-items:flex-end;gap:1px;height:10px;}
  .status-bar__signal i{display:block;width:3px;background:#fff;}
  .status-bar__carrier{position:absolute;left:30px;top:3px;}
  .status-bar__wifi{position:absolute;left:72px;top:4px;}
  .status-bar__time{position:absolute;left:0;right:0;top:3px;text-align:center;}
  .status-bar__battery{position:absolute;right:8px;top:6px;width:18px;height:8px;border:1px solid #fff;border-radius:2px;box-sizing:border-box;padding:1px;}
  .status-bar__battery::before{content:"";display:block;width:100%;height:100%;background:#fff;}
  .status-bar__battery::after{content:"";position:absolute;right:-3px;top:2px;width:2px;height:3px;background:#fff;}

  .housing{position:absolute;left:0;top:0;}

  .brand{position:absolute;left:0;right:0;top:42px;text-align:center;font-size:15px;font-weight:700;color:#cfcfcf;letter-spacing:1px;}

  .lcd{position:absolute;left:28px;top:63px;width:474px;height:46px;border-radius:8px;
    background:linear-gradient(to bottom,rgba(0,0,0,.55),rgba(0,0,0,.25));box-shadow:inset 0 1px 3px rgba(0,0,0,.8),0 1px 0 rgba(255,255,255,.15);}
  .lcd__readout{position:absolute;left:0;right:0;top:4px;text-align:center;font-family:"Share Tech Mono",monospace;color:var(--digit);font-size:38px;line-height:38px;}
  .lcd__unit{font-size:20px;}

  .slider-track{position:absolute;left:28px;top:120px;width:474px;height:3px;border-radius:2px;background:linear-gradient(#fff,#888);}
  .slider-thumb{position:absolute;left:228px;top:116px;width:11px;height:11px;border-radius:50%;background:var(--thumb);box-shadow:0 0 4px var(--thumb);}

  .wobble__label{position:absolute;left:20px;top:153px;font-size:10px;font-weight:700;color:var(--label);}
  .wobble__switch{position:absolute;left:28px;top:169px;width:62px;height:20px;border-radius:10px;background:linear-gradient(var(--lo),var(--mid));box-shadow:inset 0 1px 3px rgba(0,0,0,.7);}
  .wobble__knob{position:absolute;left:1px;top:0;width:20px;height:20px;border-radius:50%;background:radial-gradient(circle at 40% 35%,#fff,#9a9a9a);}
  .wobble__state{position:absolute;left:27px;top:4px;font-size:11px;font-weight:700;color:#fff;}

  .mode-labels{position:absolute;top:145px;font-size:11px;font-weight:700;color:var(--label);}
  .mode-labels--pink{left:172px;}
  .mode-labels--sweep{left:313px;}
  .mode-bar{position:absolute;left:132px;top:161px;width:266px;height:22px;border-radius:11px;display:flex;overflow:hidden;
    background:linear-gradient(var(--hi),var(--mid) 55%,var(--lo));box-shadow:0 1px 2px rgba(0,0,0,.8);}
  .mode-bar__btn{flex:1;text-align:center;font-size:16px;font-weight:700;color:#fff;line-height:22px;}
  .mode-bar__btn + .mode-bar__btn{border-left:1px solid rgba(0,0,0,.5);}

  .stop-label{position:absolute;left:448px;top:161px;font-size:17px;font-weight:700;color:var(--stop-text);}

  .preset-grid{position:absolute;left:24px;top:205px;width:490px;height:122px;border-radius:8px;overflow:hidden;
    display:grid;grid-template-columns:repeat(6,1fr);grid-template-rows:1fr 1fr;box-shadow:0 0 0 1px rgba(255,255,255,.12);}
  .preset{display:flex;align-items:center;justify-content:center;font-family:"Share Tech Mono",monospace;font-size:30px;color:var(--digit);
    border-right:1px solid rgba(0,0,0,.6);border-left:1px solid rgba(255,255,255,.08);}
  .preset--upper{background:linear-gradient(var(--deep),var(--lo) 60%,var(--mid));}
  .preset--lower{background:linear-gradient(var(--mid),var(--lo) 50%,var(--deep));border-top:1px solid rgba(0,0,0,.7);}
</style>
</head>
<body>

<!-- Green -->
<section class="screen screen--tl theme-green">
  <div class="status-bar"><span class="status-bar__signal"><i style="height:3px"></i><i style="height:5px"></i><i style="height:7px"></i><i style="height:10px"></i></span><span class="status-bar__carrier">Vexo</span>
    <svg class="status-bar__wifi" width="14" height="11" viewBox="0 0 14 11"><path d="M1 4a9 9 0 0 1 12 0M3.2 6.2a6 6 0 0 1 7.6 0M5.4 8.4a3 3 0 0 1 3.2 0" stroke="#fff" stroke-width="1.6" fill="none"/></svg>
    <span class="status-bar__time">12:34 PM</span><span class="status-bar__battery"></span></div>
  <svg class="housing" width="538" height="358" viewBox="0 0 538 358">
    <defs>
      <linearGradient id="body-green" x1="0" y1="0" x2="0" y2="1"><stop offset="0" style="stop-color:var(--hi)"/><stop offset=".5" style="stop-color:var(--mid)"/><stop offset="1" style="stop-color:var(--lo)"/></linearGradient>
      <linearGradient id="stop-green" x1="0" y1="0" x2="0" y2="1"><stop offset="0" style="stop-color:var(--stop-top)"/><stop offset="1" style="stop-color:var(--stop-bot)"/></linearGradient>
    </defs>
    <path d="M24 32H510Q518 32 518 40V148Q470 148 448 170Q430 190 400 190H140Q112 190 96 168Q80 150 24 150Q16 150 16 142V40Q16 32 24 32Z" fill="url(#body-green)" stroke="var(--hi)" stroke-width="1.5"/>
    <path d="M460 146H506Q514 146 514 154V186Q514 193 506 193H420Q440 146 460 146Z" fill="url(#stop-green)"/>
  </svg>
  <div class="brand">TROMP Kv</div>
  <div class="lcd"><div class="lcd__readout">32.7<span class="lcd__unit">HZ</span></div></div>
  <div class="slider-track"></div><div class="slider-thumb"></div>
  <div class="wobble__label">+10 Hz Wobble</div>
  <div class="wobble__switch"><span class="wobble__knob"></span><span class="wobble__state">OFF</span></div>
  <div class="mode-labels mode-labels--pink">Pink Noise</div><div class="mode-labels mode-labels--sweep">Sweep</div>
  <div class="mode-bar"><span class="mode-bar__btn">P</span><span class="mode-bar__btn">S</span></div>
  <div class="stop-label">STOP</div>
  <div class="preset-grid">
    <span class="preset preset--upper">20</span><span class="preset preset--upper">30</span><span class="preset preset--upper">40</span><span class="preset preset--upper">50</span><span class="preset preset--upper">60</span><span class="preset preset--upper">70</span>
    <span class="preset preset--lower">80</span><span class="preset preset--lower">90</span><span class="preset preset--lower">100</span><span class="preset preset--lower">150</span><span class="preset preset--lower">250</span><span class="preset preset--lower">300</span>
  </div>
</section>

<!-- Graphite -->
<section class="screen screen--tr theme-graphite">
  <div class="status-bar"><span class="status-bar__signal"><i style="height:3px"></i><i style="height:5px"></i><i style="height:7px"></i><i style="height:10px"></i></span><span class="status-bar__carrier">Vexo</span>
    <svg class="status-bar__wifi" width="14" height="11" viewBox="0 0 14 11"><path d="M1 4a9 9 0 0 1 12 0M3.2 6.2a6 6 0 0 1 7.6 0M5.4 8.4a3 3 0 0 1 3.2 0" stroke="#fff" stroke-width="1.6" fill="none"/></svg>
    <span class="status-bar__time">12:34 PM</span><span class="status-bar__battery"></span></div>
  <svg class="housing" width="538" height="358" viewBox="0 0 538 358">
    <defs>
      <linearGradient id="body-graphite" x1="0" y1="0" x2="0" y2="1"><stop offset="0" style="stop-color:var(--hi)"/><stop offset=".5" style="stop-color:var(--mid)"/><stop offset="1" style="stop-color:var(--lo)"/></linearGradient>
      <linearGradient id="stop-graphite" x1="0" y1="0" x2="0" y2="1"><stop offset="0" style="stop-color:var(--stop-top)"/><stop offset="1" style="stop-color:var(--stop-bot)"/></linearGradient>
    </defs>
    <path d="M24 32H510Q518 32 518 40V148Q470 148 448 170Q430 190 400 190H140Q112 190 96 168Q80 150 24 150Q16 150 16 142V40Q16 32 24 32Z" fill="url(#body-graphite)" stroke="#666" stroke-width="1.5"/>
    <path d="M460 146H506Q514 146 514 154V186Q514 193 506 193H420Q440 146 460 146Z" fill="url(#stop-graphite)"/>
  </svg>
  <div class="brand">TROMP Kv</div>
  <div class="lcd"><div class="lcd__readout">32.7<span class="lcd__unit">HZ</span></div></div>
  <div class="slider-track"></div><div class="slider-thumb"></div>
  <div class="wobble__label">+10 Hz Wobble</div>
  <div class="wobble__switch"><span class="wobble__knob"></span><span class="wobble__state">OFF</span></div>
  <div class="mode-labels mode-labels--pink">Pink Noise</div><div class="mode-labels mode-labels--sweep">Sweep</div>
  <div class="mode-bar"><span class="mode-bar__btn">P</span><span class="mode-bar__btn">S</span></div>
  <div class="stop-label">STOP</div>
  <div class="preset-grid">
    <span class="preset preset--upper">20</span><span class="preset preset--upper">30</span><span class="preset preset--upper">40</span><span class="preset preset--upper">50</span><span class="preset preset--upper">60</span><span class="preset preset--upper">70</span>
    <span class="preset preset--lower">80</span><span class="preset preset--lower">90</span><span class="preset preset--lower">100</span><span class="preset preset--lower">150</span><span class="preset preset--lower">250</span><span class="preset preset--lower">300</span>
  </div>
</section>

<!-- Blue -->
<section class="screen screen--bl theme-blue">
  <div class="status-bar"><span class="status-bar__signal"><i style="height:3px"></i><i style="height:5px"></i><i style="height:7px"></i><i style="height:10px"></i></span><span class="status-bar__carrier">Vexo</span>
    <svg class="status-bar__wifi" width="14" height="11" viewBox="0 0 14 11"><path d="M1 4a9 9 0 0 1 12 0M3.2 6.2a6 6 0 0 1 7.6 0M5.4 8.4a3 3 0 0 1 3.2 0" stroke="#fff" stroke-width="1.6" fill="none"/></svg>
    <span class="status-bar__time">12:34 PM</span><span class="status-bar__battery"></span></div>
  <svg class="housing" width="538" height="358" viewBox="0 0 538 358">
    <defs>
      <linearGradient id="body-blue" x1="0" y1="0" x2="0" y2="1"><stop offset="0" style="stop-color:var(--hi)"/><stop offset=".5" style="stop-color:var(--mid)"/><stop offset="1" style="stop-color:var(--lo)"/></linearGradient>
      <linearGradient id="stop-blue" x1="0" y1="0" x2="0" y2="1"><stop offset="0" style="stop-color:var(--stop-top)"/><stop offset="1" style="stop-color:var(--stop-bot)"/></linearGradient>
    </defs>
    <path d="M24 32H510Q518 32 518 40V148Q470 148 448 170Q430 190 400 190H140Q112 190 96 168Q80 150 24 150Q16 150 16 142V40Q16 32 24 32Z" fill="url(#body-blue)" stroke="var(--hi)" stroke-width="1.5"/>
    <path d="M460 146H506Q514 146 514 154V186Q514 193 506 193H420Q440 146 460 146Z" fill="url(#stop-blue)"/>
  </svg>
  <div class="brand">TROMP Kv</div>
  <div class="lcd"><div class="lcd__readout">32.7<span class="lcd__unit">HZ</span></div></div>
  <div class="slider-track"></div><div class="slider-thumb"></div>
  <div class="wobble__label">+10 Hz Wobble</div>
  <div class="wobble__switch"><span class="wobble__knob"></span><span class="wobble__state">OFF</span></div>
  <div class="mode-labels mode-labels--pink">Pink Noise</div><div class="mode-labels mode-labels--sweep">Sweep</div>
  <div class="mode-bar"><span class="mode-bar__btn">P</span><span class="mode-bar__btn">S</span></div>
  <div class="stop-label">STOP</div>
  <div class="preset-grid">
    <span class="preset preset--upper">20</span><span class="preset preset--upper">30</span><span class="preset preset--upper">40</span><span class="preset preset--upper">50</span><span class="preset preset--upper">60</span><span class="preset preset--upper">70</span>
    <span class="preset preset--lower">80</span><span class="preset preset--lower">90</span><span class="preset preset--lower">100</span><span class="preset preset--lower">150</span><span class="preset preset--lower">250</span><span class="preset preset--lower">300</span>
  </div>
</section>

<!-- Red -->
<section class="screen screen--br theme-red">
  <div class="status-bar"><span class="status-bar__signal"><i style="height:3px"></i><i style="height:5px"></i><i style="height:7px"></i><i style="height:10px"></i></span><span class="status-bar__carrier">Vexo</span>
    <svg class="status-bar__wifi" width="14" height="11" viewBox="0 0 14 11"><path d="M1 4a9 9 0 0 1 12 0M3.2 6.2a6 6 0 0 1 7.6 0M5.4 8.4a3 3 0 0 1 3.2 0" stroke="#fff" stroke-width="1.6" fill="none"/></svg>
    <span class="status-bar__time">12:34 PM</span><span class="status-bar__battery"></span></div>
  <svg class="housing" width="538" height="358" viewBox="0 0 538 358">
    <defs>
      <linearGradient id="body-red" x1="0" y1="0" x2="0" y2="1"><stop offset="0" style="stop-color:var(--hi)"/><stop offset=".5" style="stop-color:var(--mid)"/><stop offset="1" style="stop-color:var(--lo)"/></linearGradient>
      <linearGradient id="stop-red" x1="0" y1="0" x2="0" y2="1"><stop offset="0" style="stop-color:var(--stop-top)"/><stop offset="1" style="stop-color:var(--stop-bot)"/></linearGradient>
    </defs>
    <path d="M24 32H510Q518 32 518 40V148Q470 148 448 170Q430 190 400 190H140Q112 190 96 168Q80 150 24 150Q16 150 16 142V40Q16 32 24 32Z" fill="url(#body-red)" stroke="var(--hi)" stroke-width="1.5"/>
    <path d="M460 146H506Q514 146 514 154V186Q514 193 506 193H420Q440 146 460 146Z" fill="url(#stop-red)"/>
  </svg>
  <div class="brand">TROMP Kv</div>
  <div class="lcd"><div class="lcd__readout">32.7<span class="lcd__unit">HZ</span></div></div>
  <div class="slider-track"></div><div class="slider-thumb"></div>
  <div class="wobble__label">+10 Hz Wobble</div>
  <div class="wobble__switch"><span class="wobble__knob"></span><span class="wobble__state">OFF</span></div>
  <div class="mode-labels mode-labels--pink">Pink Noise</div><div class="mode-labels mode-labels--sweep">Sweep</div>
  <div class="mode-bar"><span class="mode-bar__btn">P</span><span class="mode-bar__btn">S</span></div>
  <div class="stop-label">STOP</div>
  <div class="preset-grid">
    <span class="preset preset--upper">20</span><span class="preset preset--upper">30</span><span class="preset preset--upper">40</span><span class="preset preset--upper">50</span><span class="preset preset--upper">60</span><span class="preset preset--upper">70</span>
    <span class="preset preset--lower">80</span><span class="preset preset--lower">90</span><span class="preset preset--lower">100</span><span class="preset preset--lower">150</span><span class="preset preset--lower">250</span><span class="preset preset--lower">300</span>
  </div>
</section>

</body>
</html>
```